Vegan Alfredo Sauce Label Design for Bramble Pantry Co

We are a food co. committed to making vegan food more accessible to people who want to eat healthier. Our first line of product is vegan Alfredo sauce.
We have 3 flavors:
- Garlic
- Pesto
- Lemony Artichoke
The current project is the design for the first flavor: garlic. However, we would like a template that would translate well to other flavors, so they look like a family of products.
These will be in standard 16 oz jars. The whole label will be approx 6cm x 24cm, but the front visual space is approx 6cm x 10cm. The rest will be nutritional labeling and copy about the company.
We also need a stamp or font- based logo that says Bramble Pantry Co. (or lower case: bramble pantry co.), the name of the company.
The picture (attached) of Vegan Mimbo is the closest to what we are going for. Because the sauce is creamy white, a colorful background with off-white font will be best.
We currently have a website, although we are doing a brand over-haul (hence, this posting) www.bramblepantryco-example.com. If the designer is a good fit, we have several more projects, in line.
Other brands we love: Tidy Acres, Marlow Ridge Foods, Pulp Poured Daily.
The final brand should communicate hip, natural and health.
And personally, I love design that is clever and somehow makes me smile.
Target Market(s)
Vegans, vegetarians, and people with common food allergies - all ages.
Young, hip families.
Industry/Entity Type
It Company
Requirements
Must have
- Copy:
Vegan Alfredo or Vegan Alfredo Sauce
Garlic
Bramble Pantry or Bramble Pantry Co
16 oz
Nice to have
- May include copy:
Gluten-Free Soy-Free Nut-Free
Should not have
- Neon colors

```html
<!DOCTYPE html>
<html lang="en">
<head>
<meta charset="utf-8">
<title>Bramble Pantry — Vegan Alfredo Sauce, Garlic</title>
<link rel="stylesheet" href="https://fonts.googleapis.com/css2?family=Caprasimo&family=Crimson+Text&family=Josefin+Sans:wght@300&family=Oswald:wght@300&display=swap">
<style>
  :root {
    --page: #ffffff;
    --teal: #3590ad;
    --dusk: #8f8aa0;
    --rose: #b57f8c;
    --rose-deep: #a97a8b;
    --logo-cream: #f6e0d3;
    --vegan-green: #93e49c;
    --alfredo-yellow: #f3e66e;
    --sauce-peach: #f6c3a6;
    --garlic-cream: #e4e7b2;
    --garlic-shadow: rgba(80, 50, 60, 0.45);
    --free-blush: #ead0cf;
    --size-white: #fbf4f2;
    --bulb-light: #f1e9ee;
    --bulb-mid: #d6bfd0;
  }
  * { margin: 0; padding: 0; box-sizing: border-box; }
  html, body {
    width: 1188px; height: 1200px; overflow: hidden; background: var(--page);
  }
  .canvas { position: relative; width: 1188px; height: 1200px; }
  .label {
    position: absolute; left: 80px; top: 80px; width: 1012px; height: 1040px;
    overflow: hidden;
    background:
      repeating-linear-gradient(152deg,
        rgba(255,255,255,0) 0px, rgba(255,255,255,0.05) 70px,
        rgba(0,0,0,0.05) 140px, rgba(255,255,255,0) 210px),
      linear-gradient(172deg, var(--teal) 0%, var(--dusk) 30%, var(--rose) 55%, var(--rose-deep) 100%);
  }
  .label > * { position: absolute; white-space: nowrap; }
  .brand-name {
    left: 166px; top: 160px;
    font-family: "Josefin Sans", sans-serif; font-weight: 300;
    font-size: 92px; letter-spacing: 4px; color: var(--logo-cream);
  }
  .product-line {
    left: 170px; top: 318px;
    font-family: "Caprasimo", serif; font-size: 56px; letter-spacing: 0.5px;
  }
  .product-line .vegan { color: var(--vegan-green); }
  .product-line .alfredo { color: var(--alfredo-yellow); margin-left: 18px; }
  .product-line .sauce { color: var(--sauce-peach); margin-left: 8px; }
  .flavor {
    left: 196px; top: 440px;
    font-family: "Caprasimo", serif; font-size: 192px; line-height: 1;
    font-weight: 400; color: var(--garlic-cream);
    text-shadow: 6px 7px 7px var(--garlic-shadow);
  }
  .allergen-list {
    left: 179px; top: 712px;
    font-family: "Crimson Text", serif; font-size: 33px; line-height: 39px;
    letter-spacing: 3px; color: var(--free-blush); list-style: none;
  }
  .allergen-free {
    left: 305px; top: 716px;
    font-family: "Oswald", sans-serif; font-weight: 300;
    font-size: 118px; line-height: 1; color: var(--free-blush);
  }
  .net-weight {
    left: 485px; top: 902px;
    font-family: "Crimson Text", serif; font-size: 24px; color: var(--size-white);
  }
  .flavor-art {
    left: 556px; top: 645px; width: 234px; height: 248px;
    border-radius: 50% 50% 46% 46% / 60% 60% 40% 40%;
    background: radial-gradient(circle at 45% 55%, var(--bulb-light) 0%, var(--bulb-mid) 100%);
  }
</style>
</head>
<body>
<main class="canvas">
  <section class="label">
    <div class="brand-name">Bramble Pantry</div>
    <div class="product-line"><span class="vegan">Vegan</span> <span class="alfredo">Alfredo</span> <span class="sauce">Sauce</span></div>
    <h1 class="flavor">Garlic</h1>
    <ul class="allergen-list">
      <li>Gluten</li>
      <li>S o y</li>
      <li>N u t</li>
    </ul>
    <div class="allergen-free">FREE</div>
    <div class="flavor-art" role="img" aria-label="Illustration of a whole garlic bulb"></div>
    <div class="net-weight">16 oz</div>
  </section>
</main>
</body>
</html>
```